CopperWanderer Stretching and Strength

We need a application design for a our first IOS application. the goal of the application is to categorize stretching and strength routines for triathlon.

We would like to see designs that use the color orange.

The design of the application should be compliant with the last version of the IOS Mobile.

For this first design we need the folowing pages:

1- Sign up
2- Log in
3- Home
4- View Exercises
5- Do it
6- Profile

The description of each page is in the attached document.

We need a logo design for the application. The logo should express that mission of the application that is for stretch and strength training for Triathlon.

We will use https://zelvanstack.example to develop the application, if you have any experience of the limitation that this technology have it will be a plus.

If you have any question please feel free to contact us.
Updates

Project Deadline Extended
Reason: We will extend the deadline to be sure that we select the best design from all of you. we will take the final decision next Tuesday.

Target Market(s)

The market for my aplicación is the Running a Triathlon world.

Logo Text

CopperWanderer

Font styles to use
Serif

Colors
f37122
ffffff
dcdcdc

Requirements
Must have
• In some future we will add more features in the menu. We should considere it for the design.
• The designs should include all the screens in the power point.

```html
<!DOCTYPE html>
<html lang="en">
<head>
<meta charset="utf-8">
<title>CopperWanderer</title>
<link rel="stylesheet" href="https://fonts.googleapis.com/css2?family=Nunito:wght@600;700;800&display=swap">
<style>
:root{
  --orange:#f37122;
  --white:#ffffff;
  --bg:#efefef;
  --tile:#f2f2f2;
  --line:#dcdcdc;
  --ink:#333333;
  --muted:#8a8a8a;
}
*{box-sizing:border-box;margin:0;padding:0}
html,body{width:756px;height:1200px;overflow:hidden}
body{font-family:"Nunito",sans-serif;background:var(--bg);position:relative}
.top-bar{position:absolute;left:0;top:0;width:756px;height:104px;
  background:linear-gradient(#ececec,#fafafa);border-top:3px solid var(--orange);
  border-bottom:1px solid #e6e6e6}
.menu-button{position:absolute;left:22px;top:32px;width:40px;height:40px;display:flex;flex-direction:column;justify-content:space-between}
.menu-button span{display:block;height:9px;border-radius:5px;background:var(--ink)}
.search-field{position:absolute;left:196px;top:30px;width:364px;height:43px;border-radius:22px;
  background:linear-gradient(#f4f4f4,#fdfdfd);border:1.5px solid #cfcfcf;
  box-shadow:inset 0 1px 3px rgba(0,0,0,.08)}
.search-field .placeholder{position:absolute;left:15px;top:8px;font-size:20px;font-weight:700;color:var(--muted)}
.search-field svg{position:absolute;right:14px;top:9px}
.hero{position:absolute;left:0;top:104px;width:756px;height:708px;
  background:radial-gradient(ellipse at 50% 55%,#ffffff 0%,#f7f7f7 45%,#ececec 100%)}
.brand-ring{position:absolute;left:290px;top:221px;width:176px;height:176px;border-radius:50%;border:11px solid var(--orange)}
.brand-name{position:absolute;left:0;width:756px;top:425px;text-align:center;
  font-size:54px;font-weight:800;color:var(--orange);letter-spacing:-.5px}
.nav-grid{position:absolute;left:0;top:812px;width:756px;height:286px;display:grid;
  grid-template-columns:378px 378px;grid-template-rows:143px 143px;
  border-top:1px solid #e2e2e2;box-shadow:0 -2px 4px rgba(0,0,0,.04)}
.nav-tile{position:relative;background:linear-gradient(#f6f6f6,#eeeeee);
  border-bottom:1px solid #dedede;display:flex;align-items:center}
.nav-tile:nth-child(odd){border-right:2px solid #e2e2e2}
.nav-icon{position:absolute;left:34px;top:24px;width:94px;height:94px;border-radius:50%;
  background:var(--white);box-shadow:0 0 3px rgba(0,0,0,.08);display:flex;align-items:center;justify-content:center}
.nav-label{position:absolute;left:145px;font-size:21px;font-weight:800;color:var(--orange);letter-spacing:.2px}
.nav-tile:nth-child(even) .nav-icon{left:36px}
.nav-tile:nth-child(even) .nav-label{left:146px}
.footer-tab{position:absolute;left:0;top:1132px;width:756px;height:68px}
</style>
</head>
<body>
<header class="top-bar">
  <div class="menu-button"><span></span><span></span><span></span></div>
  <div class="search-field">
    <span class="placeholder">Search</span>
    <svg width="28" height="28" viewBox="0 0 28 28"><circle cx="11" cy="11" r="8" fill="none" stroke="#222" stroke-width="3"/><line x1="17" y1="17" x2="25" y2="25" stroke="#222" stroke-width="4" stroke-linecap="round"/></svg>
  </div>
</header>

<section class="hero">
  <div class="brand-ring"></div>
  <h1 class="brand-name">CopperWanderer</h1>
</section>

<nav class="nav-grid">
  <div class="nav-tile">
    <div class="nav-icon">
      <svg width="60" height="56" viewBox="0 0 60 56"><path d="M30 4 L2 30 H10 V54 H24 V38 H36 V54 H50 V30 H58 Z" fill="#f37122"/><rect x="42" y="8" width="7" height="14" fill="#f37122"/></svg>
    </div>
    <span class="nav-label">HOME</span>
  </div>
  <div class="nav-tile">
    <div class="nav-icon">
      <svg width="70" height="70" viewBox="0 0 70 70" fill="none" stroke="#f37122" stroke-width="4"><rect x="2" y="2" width="28" height="36"/><rect x="38" y="2" width="28" height="20"/><rect x="2" y="46" width="28" height="22"/><rect x="38" y="30" width="28" height="38"/></svg>
    </div>
    <span class="nav-label">DASHBOARD</span>
  </div>
  <div class="nav-tile">
    <div class="nav-icon">
      <svg width="60" height="60" viewBox="0 0 60 60"><circle cx="30" cy="30" r="26" fill="none" stroke="#f37122" stroke-width="5"/><path d="M30 14 V32 H42" fill="none" stroke="#f37122" stroke-width="5" stroke-linecap="round"/></svg>
    </div>
    <span class="nav-label">REAL TIME</span>
  </div>
  <div class="nav-tile">
    <div class="nav-icon">
      <svg width="68" height="44" viewBox="0 0 68 44" fill="#f37122"><circle cx="13" cy="12" r="8"/><path d="M0 36 Q0 22 13 22 Q22 22 24 28 V36 Z"/><circle cx="55" cy="12" r="8"/><path d="M68 36 Q68 22 55 22 Q46 22 44 28 V36 Z"/><circle cx="34" cy="10" r="10" stroke="#fff" stroke-width="2"/><path d="M16 44 Q16 24 34 24 Q52 24 52 44 Z" stroke="#fff" stroke-width="2"/></svg>
    </div>
    <span class="nav-label">AUDIENCE</span>
  </div>
</nav>

<svg class="footer-tab" viewBox="0 0 756 68" preserveAspectRatio="none">
  <path d="M0 36 H104 L132 8 Q138 0 152 0 H604 Q618 0 624 8 L652 36 H756 V68 H0 Z" fill="#ffffff"/>
</svg>
</body>
</html>
```